Transportation website

I need website for my company, its gonna be transportation and logistics website, information and address, contact form , service, about

```html
<!DOCTYPE html>
<html lang="en">
<head>
<meta charset="utf-8">
<title>Harlow Transportation</title>
<link href="https://fonts.googleapis.com/css2?family=Titillium+Web:wght@400;600;700&family=Open+Sans:wght@400;600;700&display=swap" rel="stylesheet">
<style>
:root{
  --teal:#1fa99a;
  --navy:#1a2b4c;
  --navy-deep:#0e1f4d;
  --contact-bg:#0b2430;
  --ink:#2b2f36;
  --muted:#555c66;
  --line:#d8dde3;
  --white:#ffffff;
}
*{box-sizing:border-box;margin:0;padding:0}
html,body{width:1200px;height:3888px;overflow:hidden}
body{font-family:"Open Sans",Arial,sans-serif;color:var(--ink);background:var(--white);position:relative}

/* header */
.site-header{position:absolute;top:0;left:0;width:1200px;height:130px;background:var(--white);z-index:3}
.brand{position:absolute;left:145px;top:28px;display:flex;align-items:center;gap:16px}
.brand-mark{width:64px;height:64px;border-radius:50%;background:var(--teal)}
.brand-name{font-family:"Titillium Web",sans-serif;font-weight:700;color:var(--navy);font-size:30px;line-height:1;letter-spacing:4px}
.brand-name small{display:block;font-size:18px;letter-spacing:1px;margin-top:6px;font-weight:700}
.tollfree{position:absolute;left:580px;top:24px;display:flex;align-items:center;gap:10px}
.tollfree .icon{width:34px;height:34px;border-radius:50%;background:var(--teal);display:flex;align-items:center;justify-content:center}
.tollfree span{display:block;font-size:13px;color:var(--muted)}
.tollfree strong{font-size:22px;color:var(--navy);font-weight:700;line-height:1}
.search{position:absolute;left:820px;top:25px;width:236px;height:34px;border:1px solid var(--line);border-radius:17px;font-size:12px;color:#9aa0a8;padding:9px 16px}
.search svg{position:absolute;right:12px;top:8px}
.main-nav{position:absolute;left:584px;top:86px;display:flex;gap:30px;font-size:18px;font-weight:600;color:var(--navy)}

/* hero */
.hero{position:absolute;top:130px;left:0;width:1200px;height:560px;overflow:hidden;z-index:2}
.hero-photo{position:absolute;inset:0;background:linear-gradient(180deg,#7b8f98 0%,#3d5865 50%,#2e4a57 100%)}
.hero-content{position:absolute;top:190px;left:0;width:1200px;text-align:center;color:var(--white)}
.hero-content h1{font-family:"Titillium Web",sans-serif;font-weight:700;font-size:54px;letter-spacing:1px;line-height:1}
.hero-content p{font-size:17px;line-height:30px;margin-top:22px}
.hero-call{display:inline-flex;align-items:center;gap:14px;margin-top:22px;background:var(--teal);border-radius:30px;padding:8px 34px 8px 8px;font-size:26px;font-weight:700}
.hero-call .icon{width:40px;height:40px;border-radius:50%;background:var(--white);display:flex;align-items:center;justify-content:center}
.slider-dots{position:absolute;top:532px;left:564px;display:flex;gap:10px}
.slider-dots i{width:16px;height:16px;border-radius:50%;border:2px solid var(--white)}
.slider-dots i.active{background:var(--white)}

/* welcome */
.welcome{position:absolute;top:690px;left:0;width:1200px;height:662px;background:linear-gradient(90deg,#f5efec 0%,#fbf6f4 100%)}
.welcome-photo{position:absolute;left:0;top:0;width:700px;height:662px;background:linear-gradient(100deg,#7a3a22 0%,#a8502d 35%,#9fb8cc 65%,rgba(251,246,244,0) 100%)}
.hero-wave{position:absolute;top:650px;left:0;width:1200px;height:130px;z-index:3}
.welcome-text{position:absolute;left:622px;top:180px;width:500px}
.welcome-text h2{font-family:"Titillium Web",sans-serif;font-weight:700;font-size:38px;line-height:48px;color:var(--navy)}
.welcome-text h2 span{display:block;color:var(--teal);white-space:nowrap}
.rule{width:92px;height:4px;background:var(--teal);margin:22px 0 26px}
.welcome-text p{font-size:15px;line-height:33px;color:var(--ink);width:440px}
.btn-outline{display:inline-block;margin-top:34px;border:2px solid var(--navy);border-radius:22px;padding:9px 32px;font-size:14px;font-weight:700;color:var(--navy)}

/* services */
.services{position:absolute;top:1352px;left:0;width:1200px;height:624px;background:linear-gradient(120deg,#24437a 0%,#1d5b7e 40%,#1a8a8d 75%,#17a092 100%);color:var(--white);text-align:center}
.services h2{font-family:"Titillium Web",sans-serif;font-weight:400;font-size:44px;margin-top:80px;line-height:1}
.services h2 b{font-weight:700}
.services .rule{background:var(--white);margin:24px auto 0;width:64px}
.service-list{position:absolute;top:220px;left:97px;display:flex}
.service{width:252px}
.service-icon{width:128px;height:128px;border-radius:50%;background:var(--white);border:5px solid #c8e9e5;margin:0 auto;display:flex;align-items:center;justify-content:center}
.service h3{font-family:"Titillium Web",sans-serif;font-size:17px;font-weight:700;margin-top:20px;letter-spacing:.3px}
.service p{font-size:13px;line-height:23px;margin:12px auto 0;width:220px}
.btn-small{display:inline-block;margin-top:22px;border:2px solid var(--white);border-radius:16px;padding:5px 22px;font-size:11px;font-weight:700}

/* contact */
.contact{position:absolute;top:1976px;left:0;width:1200px;height:646px;background:var(--contact-bg);color:var(--white)}
.contact-photo{position:absolute;left:0;top:0;width:580px;height:646px;background:linear-gradient(90deg,#1d4a63 0%,#163a4e 60%,#0b2430 100%)}
.contact-body{position:absolute;left:635px;top:72px;width:422px}
.contact-body h2{font-family:"Titillium Web",sans-serif;font-size:34px;font-weight:700;line-height:1}
.contact-body .rule{background:var(--white);width:74px;margin:20px 0 26px}
.contact-body p{font-size:16px}
.field{margin-top:26px;background:var(--white);height:40px;font-size:13px;color:#555;padding:11px 12px}
.field+.field{margin-top:16px}
.field.textarea{height:98px}
.btn-submit{display:inline-block;margin-top:20px;width:220px;height:46px;background:var(--teal);text-align:center;line-height:46px;font-weight:700;font-size:16px;letter-spacing:.5px}

/* news */
.news{position:absolute;top:2622px;left:0;width:1200px;height:700px;background:var(--white);text-align:center}
.news h2{font-family:"Titillium Web",sans-serif;font-size:44px;font-weight:700;color:var(--navy);margin-top:86px;line-height:1}
.news h2 span{color:var(--teal)}
.news .rule{margin:26px auto 0;width:78px}
.news-list{position:absolute;top:216px;left:134px;display:flex;gap:32px}
.news-card{width:292px}
.news-photo{height:192px}
.news-body{width:264px;margin:-20px auto 0;background:var(--white);box-shadow:0 3px 14px rgba(0,0,0,.16);padding:26px 18px 28px;position:relative}
.news-body h3{font-size:18px;font-weight:600;line-height:25px;color:var(--navy)}
.news-date{margin-top:14px;color:var(--teal);font-size:16px;display:flex;justify-content:center;align-items:center;gap:8px}
.news-body p{font-size:12px;line-height:21px;margin-top:14px;color:var(--ink)}

/* footer */
.footer-wave{position:absolute;top:3300px;left:0;width:1200px;height:160px}
.site-footer{position:absolute;top:3440px;left:0;width:1200px;height:448px;background:var(--navy-deep);color:var(--white)}
.footer-col{position:absolute;top:36px}
.footer-col h4{font-family:"Titillium Web",sans-serif;font-size:24px;font-weight:700;letter-spacing:.3px}
.contact-col{left:143px;width:300px}
.contact-item{display:flex;gap:12px;font-size:13px;line-height:21px;margin-top:24px;align-items:flex-start}
.contact-item:first-of-type{margin-top:34px}
.contact-item svg{flex:none;margin-top:2px}
.links-col{left:476px}
.links-col ul{list-style:none;margin-top:26px;font-size:13px;line-height:28px}
.news-col{left:673px;width:380px}
.news-col p{font-size:13px;margin-top:28px}
.subscribe{display:flex;gap:12px;margin-top:20px}
.subscribe .input{width:258px;height:38px;background:var(--white);color:#777;font-size:12px;padding:11px 12px}
.subscribe .btn{width:112px;height:38px;background:var(--teal);font-size:12px;font-weight:700;text-align:center;line-height:38px}
.news-col h5{font-size:12px;font-weight:700;margin-top:36px}
.social{display:flex;gap:6px;margin-top:16px}
.social i{width:18px;height:18px;background:var(--white);border-radius:2px}
.footer-bottom{position:absolute;top:338px;left:0;width:1200px;border-top:1px solid rgba(255,255,255,.25);text-align:center;font-size:14px;padding-top:44px}
</style>
</head>
<body>

<header class="site-header">
  <div class="brand">
    <div class="brand-mark"></div>
    <div class="brand-name">HARLOW<small>TRANSPORTATION</small></div>
  </div>
  <div class="tollfree">
    <div class="icon"><svg width="18" height="18" viewBox="0 0 24 24"><path fill="#fff" d="M6.6 10.8a15 15 0 0 0 6.6 6.6l2.2-2.2a1 1 0 0 1 1-.25 11.4 11.4 0 0 0 3.6.57 1 1 0 0 1 1 1V20a1 1 0 0 1-1 1A17 17 0 0 1 3 4a1 1 0 0 1 1-1h3.5a1 1 0 0 1 1 1c0 1.25.2 2.450.57 3.57a1 1 0 0 1-.25 1z"/></svg></div>
    <div><span>Toll free :</span><strong>0300 555 0142</strong></div>
  </div>
  <div class="search">Search here
    <svg width="16" height="16" viewBox="0 0 24 24"><circle cx="10" cy="10" r="7" fill="none" stroke="#7a8089" stroke-width="2.4"/><path d="M15 15l6 6" stroke="#7a8089" stroke-width="2.4"/></svg>
  </div>
  <nav class="main-nav"><span>Home</span><span>About Us</span><span>Our Services</span><span>Blog</span><span>Contact Us</span></nav>
</header>

<section class="hero">
  <div class="hero-photo" role="img" aria-label="Aerial photo of a container ship sailing out of a harbour"></div>
  <div class="hero-content">
    <h1>HARLOW TRANSPORTATION</h1>
    <p>Sed ut perspiciatis unde omnis iste natus error sit voluptatem accusantium<br>doloremque laudantium, totam rem aperiam, eaque ipsa quae</p>
    <div class="hero-call"><span class="icon"><svg width="22" height="22" viewBox="0 0 24 24"><path fill="#1fa99a" d="M6.6 10.8a15 15 0 0 0 6.6 6.6l2.2-2.2a1 1 0 0 1 1-.25 11.4 11.4 0 0 0 3.6.57 1 1 0 0 1 1 1V20a1 1 0 0 1-1 1A17 17 0 0 1 3 4a1 1 0 0 1 1-1h3.5a1 1 0 0 1 1 1c0 1.25.2 2.45.57 3.57a1 1 0 0 1-.25 1z"/></svg></span>0300 555 0142</div>
  </div>
  <div class="slider-dots"><i class="active"></i><i></i><i></i></div>
</section>

<section class="welcome">
  <div class="welcome-photo" role="img" aria-label="Photo of a red container truck driving along a coastal road"></div>
  <div class="welcome-text">
    <h2>Welcome to<span>HARLOW TRANSPORTATION</span></h2>
    <div class="rule"></div>
    <p>Sed ut perspiciatis unde omnis iste natus error sit vtatem accusantium doloremque laudantium, totam rem aperiam, eaque ipsa quae ab illo inventore veritatis et quasi architecto beatae vitae dicta sunt explicabo. Nemo enim ipsam vptatem quia voluptas sit aspernatur aut odit</p>
    <span class="btn-outline">READ MORE</span>
  </div>
</section>

<svg class="hero-wave" viewBox="0 0 1200 130" preserveAspectRatio="none">
  <path d="M60 118 C420 96 860 80 1200 10" fill="none" stroke="#1a2b4c" stroke-width="6"/>
  <path d="M120 126 C480 112 880 96 1200 30" fill="none" stroke="#1fa99a" stroke-width="5"/>
</svg>

<section class="services">
  <h2><b>OUR</b> SERVICES</h2>
  <div class="rule"></div>
  <div class="service-list">
    <div class="service">
      <div class="service-icon"><svg width="64" height="64" viewBox="0 0 64 64"><rect x="14" y="10" width="34" height="44" rx="3" fill="none" stroke="#1a2b4c" stroke-width="3"/><rect x="24" y="6" width="14" height="8" rx="2" fill="#1a2b4c"/><path d="M20 24h20M20 32h20M20 40h12" stroke="#1a2b4c" stroke-width="3"/><circle cx="46" cy="46" r="10" fill="#1fa99a"/><path d="M41 46l4 4 6-7" fill="none" stroke="#fff" stroke-width="3"/></svg></div>
      <h3>CONTRACT LOGISTICS</h3>
      <p>Sed ut perspiciatis unde omnis iste natus error sit voluptatem santium doloremque udantium, totam</p>
      <span class="btn-small">READ MORE</span>
    </div>
    <div class="service">
      <div class="service-icon"><svg width="64" height="64" viewBox="0 0 64 64"><circle cx="32" cy="32" r="24" fill="#1a2b4c"/><path d="M16 26c6 2 10-4 16-2s4 8 10 6M20 42c4-2 8 0 12 4" fill="none" stroke="#1fa99a" stroke-width="4"/></svg></div>
      <h3>FAST TRANSPORTATION</h3>
      <p>Sed ut perspiciatis unde omnis iste natus error sit voluptatem santium doloremque udantium, totam</p>
      <span class="btn-small">READ MORE</span>
    </div>
    <div class="service">
      <div class="service-icon"><svg width="64" height="64" viewBox="0 0 64 64"><circle cx="34" cy="28" r="20" fill="none" stroke="#1a2b4c" stroke-width="3"/><path d="M34 16v12l8 5" fill="none" stroke="#1a2b4c" stroke-width="3"/><rect x="8" y="42" width="22" height="12" fill="#1fa99a"/><path d="M30 46h8l4 4v4H30z" fill="#1fa99a"/><circle cx="14" cy="56" r="3" fill="#1a2b4c"/><circle cx="36" cy="56" r="3" fill="#1a2b4c"/></svg></div>
      <h3>SHIPPING WORLDWIDE</h3>
      <p>Sed ut perspiciatis unde omnis iste natus error sit voluptatem santium doloremque udantium, totam</p>
      <span class="btn-small">READ MORE</span>
    </div>
    <div class="service">
      <div class="service-icon"><svg width="64" height="64" viewBox="0 0 64 64"><rect x="22" y="10" width="22" height="22" rx="2" fill="#1fa99a"/><path d="M33 15v12M27 21h12" stroke="#fff" stroke-width="3"/><path d="M6 40h12c6 0 10 4 16 4h10a3 3 0 0 1 0 6H30M18 54c8 2 18 2 26-2l14-8a3 3 0 0 0-4-5l-10 5" fill="none" stroke="#1a2b4c" stroke-width="3"/></svg></div>
      <h3>SAFETY &amp; RELIABILITY</h3>
      <p>Sed ut perspiciatis unde omnis iste natus error sit voluptatem santium doloremque udantium, totam</p>
      <span class="btn-small">READ MORE</span>
    </div>
  </div>
</section>

<section class="contact">
  <div class="contact-photo" role="img" aria-label="Aerial photo of a cargo ship loaded with containers at sea"></div>
  <div class="contact-body">
    <h2>CONTACT FORM</h2>
    <div class="rule"></div>
    <p>Sed ut perspiciatis unde omnis iste natus</p>
    <div class="field">Name</div>
    <div class="field">Email address</div>
    <div class="field">Phone number</div>
    <div class="field textarea">Comment</div>
    <span class="btn-submit">SUBMIT</span>
  </div>
</section>

<section class="news">
  <h2>LATEST <span>NEWS</span></h2>
  <div class="rule"></div>
  <div class="news-list">
    <article class="news-card">
      <div class="news-photo" role="img" aria-label="Photo of port cranes and containers at sunset" style="background:linear-gradient(160deg,#3b5d86 0%,#e4893a 55%,#8a3b2a 100%)"></div>
      <div class="news-body">
        <h3>Sed ut perspiciatis unde omnis iste natus</h3>
        <div class="news-date"><svg width="14" height="14" viewBox="0 0 14 14"><rect x="1" y="2" width="12" height="11" fill="none" stroke="#1fa99a" stroke-width="1.6"/><path d="M1 5h12" stroke="#1fa99a" stroke-width="1.6"/></svg>Oct 01, 2019</div>
        <p>Sed ut perspiciatis unde omnis iste natus error sit voluptatem accusantium donque laudantium, totam</p>
      </div>
    </article>
    <article class="news-card">
      <div class="news-photo" role="img" aria-label="Photo of a city skyline at dusk with network lights" style="background:linear-gradient(180deg,#2f6b8a 0%,#1b3f5c 60%,#3f7a7e 100%)"></div>
      <div class="news-body">
        <h3>Sed ut perspiciatis unde omnis iste natus</h3>
        <div class="news-date"><svg width="14" height="14" viewBox="0 0 14 14"><rect x="1" y="2" width="12" height="11" fill="none" stroke="#1fa99a" stroke-width="1.6"/><path d="M1 5h12" stroke="#1fa99a" stroke-width="1.6"/></svg>Oct 01, 2019</div>
        <p>Sed ut perspiciatis unde omnis iste natus error sit voluptatem accusantium donque laudantium, totam</p>
      </div>
    </article>
    <article class="news-card">
      <div class="news-photo" role="img" aria-label="Photo of hands working on a laptop with logistics graphics" style="background:linear-gradient(150deg,#4a5a6c 0%,#8d98a6 50%,#2b3846 100%)"></div>
      <div class="news-body">
        <h3>Sed ut perspiciatis unde omnis iste natus</h3>
        <div class="news-date"><svg width="14" height="14" viewBox="0 0 14 14"><rect x="1" y="2" width="12" height="11" fill="none" stroke="#1fa99a" stroke-width="1.6"/><path d="M1 5h12" stroke="#1fa99a" stroke-width="1.6"/></svg>Oct 01, 2019</div>
        <p>Sed ut perspiciatis unde omnis iste natus error sit voluptatem accusantium donque laudantium, totam</p>
      </div>
    </article>
  </div>
</section>

<svg class="footer-wave" viewBox="0 0 1200 160" preserveAspectRatio="none">
  <path d="M0 160 C300 50 850 30 1200 150 V160 Z" fill="#0e1f4d"/>
  <path d="M40 145 C330 40 860 20 1150 130" fill="none" stroke="#1fa99a" stroke-width="6"/>
  <path d="M0 160 C300 60 860 40 1200 152" fill="none" stroke="#1a2b4c" stroke-width="4"/>
</svg>

<footer class="site-footer">
  <div class="footer-col contact-col">
    <h4>CONTACT US</h4>
    <div class="contact-item"><svg width="14" height="18" viewBox="0 0 14 18"><path d="M7 1a6 6 0 0 0-6 6c0 5 6 10 6 10s6-5 6-10a6 6 0 0 0-6-6z" fill="none" stroke="#fff" stroke-width="1.6"/><circle cx="7" cy="7" r="2" fill="#fff"/></svg><span>24-28 Harlow Way<br>Northgate, Victoria 3150, UK.</span></div>
    <div class="contact-item"><svg width="16" height="16" viewBox="0 0 24 24"><path fill="#fff" d="M6.6 10.8a15 15 0 0 0 6.6 6.6l2.2-2.2a1 1 0 0 1 1-.25 11.4 11.4 0 0 0 3.6.57 1 1 0 0 1 1 1V20a1 1 0 0 1-1 1A17 17 0 0 1 3 4a1 1 0 0 1 1-1h3.5a1 1 0 0 1 1 1c0 1.25.2 2.45.57 3.57a1 1 0 0 1-.25 1z"/></svg><span>Phone: 0300 555 0142</span></div>
    <div class="contact-item"><svg width="16" height="16" viewBox="0 0 16 16"><rect x="1" y="6" width="14" height="8" fill="#fff"/><rect x="4" y="1" width="8" height="5" fill="none" stroke="#fff" stroke-width="1.6"/></svg><span>Fax: 0300 555 0142</span></div>
    <div class="contact-item"><svg width="16" height="14" viewBox="0 0 16 14"><rect x="1" y="2" width="14" height="10" fill="none" stroke="#fff" stroke-width="1.6"/><path d="M1 2l7 6 7-6" fill="none" stroke="#fff" stroke-width="1.6"/></svg><span>Email: info@harlowtransport.example</span></div>
  </div>
  <div class="footer-col links-col">
    <h4>QUICK LINKS</h4>
    <ul><li>Home</li><li>About Us</li><li>Our Services</li><li>Blog</li><li>Support</li><li>Contact Us</li></ul>
  </div>
  <div class="footer-col news-col">
    <h4>SIGN UP FOR NEWSLETTER</h4>
    <p>Sign up to our mailing list</p>
    <div class="subscribe"><div class="input">Enter email</div><div class="btn">SUBSCRIPTION</div></div>
    <h5>STAY CONNECTED WITH US</h5>
    <div class="social"><i></i><i></i><i></i></div>
  </div>
  <div class="footer-bottom">(c) 2019 Harlow Transportation | All Rights Reserved | Terms and Conditions</div>
</footer>

</body>
</html>
```